Poster Design Project

About Us
Lumvik is a company that specializes in providing communication solutions to the travel market. Our simple vision of “every hotel should have a mobile phone in the guest rooms”, led us to develop a path breaking cost effective mobile phone. With full integration capabilities with the hotels property management system, location based marketing, user locator and other features, this product is unique in addressing the hospitality segment.
Product Placement
The Lumvik mobile will be placed in the hotel room on an A4 Sized transparent stand (the transparent stand is attached for your reference. If you notice, the phone will be placed in the jacket on the bottom left and in another jacket on the bottom right will be the brochure. So effectively, the design space available on the A4 brochure is only 60% of the space). The designed poster that we wish designed will be inserted in the A4 sized acrylic stand. The stand would typically be on the bedside table or on the study table of the hotel room. The A4 design should be bright and vibrant in keeping with our logo colors.
Attached is our logo. Also attached is the symbol of our phone that could be used innovatively on the brochure if you think it helps.
Attached is the content for the poster.
Reason: Feedback from the management team got delayed, hence the extension. Thanks
Reason: The delay is in the content finalization.

```html
<!DOCTYPE html>
<html lang="en">
<head>
<meta charset="utf-8">
<title>Lumvik – Keep Talking Poster</title>
<link rel="stylesheet" href="https://fonts.googleapis.com/css2?family=Montserrat:wght@400;600;700&display=swap">
<style>
  :root {
    --poster-orange: #fb9b2e;
    --ink: #22141e;
  }
  * { margin: 0; padding: 0; box-sizing: border-box; }
  html, body {
    width: 848px;
    height: 1200px;
    overflow: hidden;
    background: var(--poster-orange);
  }
  .poster {
    position: relative;
    width: 848px;
    height: 1200px;
    background: var(--poster-orange);
    color: var(--ink);
    font-family: "Montserrat", Arial, sans-serif;
  }
  .brand {
    position: absolute;
    left: 56px;
    top: 50px;
    display: inline-flex;
    flex-direction: column;
    align-items: flex-end;
  }
  .brand-name {
    font-size: 80px;
    font-weight: 700;
    line-height: 1;
    letter-spacing: -1px;
  }
  .brand-tagline {
    font-size: 19px;
    font-weight: 600;
    line-height: 1;
    margin-top: 4px;
  }
  .line {
    position: absolute;
    left: 0;
    width: 100%;
    text-align: center;
    line-height: 1;
    white-space: nowrap;
    font-weight: 700;
  }
  .headline-call { top: 226px; font-size: 60px; letter-spacing: -0.5px; }
  .headline-talk { top: 292px; font-size: 76px; letter-spacing: -0.5px; text-align: left; left: 74px; width: auto; }
  .features { top: 375px; font-size: 14px; font-weight: 400; letter-spacing: 0; }
  .offer-roaming { top: 461px; font-size: 37px; }
  .offer-item { font-size: 35px; }
  .offer-international { top: 579px; }
  .offer-local { top: 631px; }
  .offer-number { top: 683px; }
  .price { top: 797px; font-size: 49px; }
</style>
</head>
<body>
  <main class="poster">
    <header class="brand">
      <span class="brand-name">Lumvik</span>
      <span class="brand-tagline">keep talking</span>
    </header>

    <h1 class="line headline-call">Pick up the phone NOW</h1>
    <h2 class="line headline-talk">and keep talking...</h2>
    <p class="line features">Itemized bill on checkout, Flexible tariff plans to choose from, Excellent call quality.</p>

    <p class="line offer-roaming">save 80% on international roaming</p>

    <p class="line offer-item offer-international">60 FREE minutes of international calls</p>
    <p class="line offer-item offer-local">60 FREE minutes of local calls</p>
    <p class="line offer-item offer-number">get a LOCAL number</p>

    <p class="line price">for just 499 BHT</p>
  </main>
</body>
</html>
```